Webpage layout and company logo combination

We are trying to renovate an existing site to make it sharper and sophisticated in appearance. This is the existing site: http://www.pellmoorrealtynj.com/agents.html . The new presentation should be bright, sharp, sophisticated and should incorporate two additional menu tabs. The menu tabs will be revised as follows: Property Listings, Property Management, Advisory & Consulting, Local Info, R/E Tools, Our Team (please disregard Korean language characters, which will be installed after English version is completed, separately).

It Company

```html
<!DOCTYPE html>
<html lang="en">
<head>
<meta charset="utf-8">
<title>Pellmoor Realty</title>
<link href="https://fonts.googleapis.com/css2?family=Roboto:ital,wght@0,300;0,400;0,500;0,700;1,400&family=Open+Sans:wght@400;600&display=swap" rel="stylesheet">
<style>
:root{
  --sage:#b9c48c;
  --sage-dark:#a7b378;
  --sage-light:#cdd5a7;
  --plum:#8d3a5b;
  --plum-deep:#6f2a46;
  --rose:#a9456d;
  --ink:#3d3d3d;
  --muted:#7a7a7a;
  --paper:#ffffff;
  --mist:#efefef;
  --cream:#f7f3dc;
}
*{margin:0;padding:0;box-sizing:border-box}
html,body{width:1200px;height:3032px;overflow:hidden}
body{font-family:"Open Sans",Arial,sans-serif;color:var(--ink);background:var(--paper);position:relative;font-size:13px}
h1,h2,h3,h4,.nav a,.brand{font-family:"Roboto",Arial,sans-serif}
section,header,nav,footer{position:absolute;left:0;width:1200px}
.abs{position:absolute}

/* header */
.site-header{top:0;height:88px;background:linear-gradient(var(--sage-light),var(--sage))}
.brand{left:172px;top:24px;display:flex;align-items:center;gap:10px;font-size:34px;font-weight:700;color:var(--plum-deep)}
.brand-mark{width:30px;height:30px;background:var(--plum-deep)}
.phone{right:172px;top:32px;display:flex;align-items:center;gap:10px;color:#fff;font-family:"Roboto",sans-serif;font-size:20px}
.main-nav{top:88px;height:38px;background:linear-gradient(var(--rose),var(--plum));display:flex;justify-content:center;align-items:center}
.main-nav a{color:#fff;text-decoration:none;font-size:13px;font-weight:500;padding:0 16px;border-right:1px solid rgba(255,255,255,.35);line-height:16px}
.main-nav a:last-child{border-right:0}

/* hero */
.hero{top:126px;height:430px}
.hero-photo{position:absolute;inset:0;background:linear-gradient(160deg,#5a4a5e 0%,#8c6a58 35%,#c79a6a 55%,#3f6f7a 80%,#2b3d48 100%)}
.search-box{left:715px;top:56px;width:303px;height:273px;background:rgba(255,255,255,.82);padding:14px 18px}
.search-box h2{font-size:26px;font-weight:700;color:var(--plum);text-align:center}
.search-box .rule{height:2px;background:var(--plum);width:150px;margin:6px auto 10px}
.field{height:26px;background:#fff;border:1px solid #ccc;margin-bottom:10px;font-size:12px;color:#999;padding:4px 8px;position:relative}
.field::after{content:"";position:absolute;right:4px;top:5px;width:14px;height:14px;background:#555}
.pair{display:flex;gap:10px}.pair .field{flex:1}
.search-btn{height:36px;background:var(--sage-dark);color:#fff;text-align:center;line-height:36px;font-family:"Roboto",sans-serif;font-weight:700;letter-spacing:2px;font-size:16px}
.dots{left:0;top:450px;width:1200px;display:flex;justify-content:center;gap:5px}
.dots i{width:10px;height:10px;border-radius:50%;background:#fff;display:block}
.dots i:first-child{background:var(--rose)}

/* services */
.services{top:556px;height:349px;background:var(--sage)}
.service{top:80px;width:200px;text-align:center;color:#fff}
.service .hex{margin:0 auto}
.service h3{font-size:17px;font-weight:700;color:var(--plum-deep);margin:12px 0 8px}
.service p{font-size:11px;line-height:15px}
.service a{display:block;margin-top:18px;color:var(--plum-deep);font-size:11px;text-decoration:underline}
.divider{top:60px;width:2px;height:240px;background:linear-gradient(transparent,rgba(255,255,255,.6),transparent)}

/* welcome */
.welcome{top:905px;height:353px;background:linear-gradient(#fff 40%,var(--mist))}
.skyline{left:0;bottom:0;width:1200px;height:150px;background:linear-gradient(transparent,#e2e2e2);opacity:.8}
.welcome h1{position:absolute;top:50px;width:100%;text-align:center;font-size:28px;font-weight:500;color:var(--rose)}
.welcome p{position:absolute;left:172px;width:856px;text-align:center;font-size:12px;line-height:17px;color:var(--muted)}
.btn{display:inline-block;background:linear-gradient(var(--rose),var(--plum));color:#fff;font-size:13px;font-weight:600;text-align:center;border-radius:3px;width:132px;height:32px;line-height:32px}

/* advisory & agents */
.advisory{top:1258px;height:536px}
.advisory h2{font-size:30px;font-weight:500;color:var(--rose)}
.team h2{font-size:24px;font-weight:700;color:var(--plum-deep)}
.adv-photo{left:172px;top:112px;width:194px;height:210px}
.adv-text{left:379px;top:140px;width:185px;font-size:11px;line-height:15px;color:var(--muted)}
.adv-text h3{font-size:19px;font-weight:400;color:var(--rose);margin-bottom:8px}
.adv-text .hl{color:var(--sage-dark);margin:12px 0}
.agent{left:614px;display:flex;gap:20px;width:420px}
.agent .avatar{width:80px;height:80px;border-radius:50%;border:3px solid #ddd;flex:none}
.agent h4{font-family:"Roboto",sans-serif;font-style:italic;font-weight:400;color:var(--rose);font-size:14px;margin-bottom:6px}
.agent p{font-size:11px;line-height:15px;color:var(--muted)}
.agent a{font-size:11px;color:var(--sage-dark);text-decoration:underline;display:block;margin-top:6px}

/* why */
.why{top:1794px;height:424px}
.why-photo{position:absolute;inset:0;background:linear-gradient(90deg,#8a4a60,#a46a78 50%,#7e3c55)}
.why h2{position:absolute;top:46px;width:100%;text-align:center;color:#fff;font-size:30px;font-weight:700}
.why .sub{position:absolute;top:102px;width:100%;text-align:center;color:#fff;font-family:"Roboto",sans-serif;font-weight:300;font-size:30px}
.why-col{top:280px;width:270px;color:#fff}
.why-col h3{font-size:30px;font-weight:700}
.why-col h3 span{font-size:20px;margin-right:8px}
.why-col p{font-size:11px;line-height:15px;margin-top:6px}

/* testimonials */
.testimonials{top:2218px;height:485px}
.testimonials h2{position:absolute;top:52px;width:100%;text-align:center;font-size:30px;font-weight:700;color:var(--plum-deep)}
.testimonials h3{position:absolute;top:98px;width:100%;text-align:center;font-size:30px;font-weight:400;color:var(--rose)}
.quote{top:182px;height:215px;border:1px solid #ddd;border-radius:8px;padding:18px;font-size:11px;line-height:16px;color:var(--muted)}
.client{top:344px;display:flex;align-items:center;gap:18px;font-size:11px;color:var(--muted)}
.client .avatar{width:62px;height:62px;border-radius:50%;border:3px solid #fff;box-shadow:0 0 0 1px #ccc}

/* footer */
.site-footer{top:2703px;height:285px;background:var(--sage);color:#fff}
.f-col{top:38px;width:260px}
.f-col h4{font-size:19px;font-weight:400;display:flex;align-items:center;gap:10px;padding-bottom:10px;border-bottom:1px solid rgba(255,255,255,.5);margin-bottom:14px}
.f-col h4 i{width:24px;height:20px;border:2px solid #fff;display:block}
.news .date{color:var(--plum-deep);font-size:11px}
.news p{font-size:11px;line-height:14px;margin-bottom:14px}
.contact li{list-style:none;display:flex;gap:12px;font-size:11px;margin-bottom:12px}
.contact li i{width:16px;height:14px;background:#fff;display:block;flex:none}
.socials{display:flex;gap:8px;margin-top:4px}
.socials span{width:22px;height:22px;border-radius:50%;background:#fff;display:block}
.sub-field{height:28px;background:#fff;color:#aaa;font-size:11px;padding:6px 10px;margin:12px 0}
.sub-row{display:flex;justify-content:space-between;align-items:center}
.sub-brand{font-family:"Roboto",sans-serif;font-weight:700;font-size:20px;color:var(--plum-deep)}
.sub-btn{background:var(--plum);color:#fff;font-size:12px;padding:8px 16px;border-radius:3px}
.copyright{top:2988px;height:44px;background:var(--plum-deep);color:#fff;text-align:center;line-height:44px;font-size:11px}
</style>
</head>
<body>

<header class="site-header">
  <div class="brand abs"><span class="brand-mark"></span>Pellmoor Realty</div>
  <div class="phone abs">
    <svg width="20" height="20" viewBox="0 0 20 20"><circle cx="10" cy="10" r="9" fill="none" stroke="#fff" stroke-width="1.6"/><path d="M7 5l2 3-1 1c.6 1.4 1.6 2.4 3 3l1-1 3 2-1 2c-4 0-8-4-8-8z" fill="#fff"/></svg>
    (866) 555-0142
  </div>
</header>

<nav class="main-nav">
  <a href="#">About Us</a><a href="#">Property Listings</a><a href="#">Property Management</a><a href="#">Advisory &amp; Consulting</a><a href="#">Local Info</a><a href="#">R/E Tools</a><a href="#">Our Team</a><a href="#">Contact Us</a>
</nav>

<section class="hero">
  <div class="hero-photo" role="img" aria-label="Luxury home with lit pool at dusk"></div>
  <form class="search-box abs">
    <h2>Find Your Dream Home</h2>
    <div class="rule"></div>
    <div class="field">City</div>
    <div class="field">Property Type</div>
    <div class="pair"><div class="field">Price Min</div><div class="field">Price Max</div></div>
    <div class="search-btn">SEARCH HOME</div>
  </form>
  <div class="dots abs"><i></i><i></i><i></i></div>
</section>

<section class="services">
  <div class="service abs" style="left:173px">
    <svg class="hex" width="82" height="90" viewBox="0 0 82 90"><polygon points="41,2 79,24 79,66 41,88 3,66 3,24" fill="var(--plum)" stroke="#fff" stroke-width="3"/><path d="M24 34h6l6 18h16l4-12H33" fill="none" stroke="#fff" stroke-width="3"/><circle cx="38" cy="58" r="3" fill="#fff"/><circle cx="50" cy="58" r="3" fill="#fff"/></svg>
    <h3>Selling</h3>
    <p>Duis venenatis nibh ac convallis laoreet. In dignissim imperdiet feugiat. Integer blandit tortor tellus, sed sodales ligula tristique et.</p>
    <a href="#">Read more »</a>
  </div>
  <div class="divider abs" style="left:384px"></div>
  <div class="service abs" style="left:390px">
    <svg class="hex" width="82" height="90" viewBox="0 0 82 90"><polygon points="41,2 79,24 79,66 41,88 3,66 3,24" fill="var(--plum)" stroke="#fff" stroke-width="3"/><rect x="25" y="34" width="32" height="22" fill="none" stroke="#fff" stroke-width="3"/><path d="M41 26v8" stroke="#fff" stroke-width="3"/></svg>
    <h3>Buying</h3>
    <p>Duis venenatis nibh ac convallis laoreet. In dignissim imperdiet feugiat. Integer blandit tortor tellus, sed sodales ligula tristique et.</p>
    <a href="#">Read more »</a>
  </div>
  <div class="divider abs" style="left:599px"></div>
  <div class="service abs" style="left:607px">
    <svg class="hex" width="82" height="90" viewBox="0 0 82 90"><polygon points="41,2 79,24 79,66 41,88 3,66 3,24" fill="var(--plum)" stroke="#fff" stroke-width="3"/><path d="M34 30h14l-3 6c8 4 11 10 11 16 0 5-6 6-15 6s-15-1-15-6c0-6 3-12 11-16z" fill="#fff"/><text x="41" y="54" text-anchor="middle" font-size="13" font-weight="700" fill="var(--plum)" font-family="Roboto,sans-serif">$</text></svg>
    <h3>Investing</h3>
    <p>Duis venenatis nibh ac convallis laoreet. In dignissim imperdiet feugiat. Integer blandit tortor tellus, sed sodales ligula tristique et.</p>
    <a href="#">Read more »</a>
  </div>
  <div class="divider abs" style="left:816px"></div>
  <div class="service abs" style="left:825px">
    <svg class="hex" width="82" height="90" viewBox="0 0 82 90"><polygon points="41,2 79,24 79,66 41,88 3,66 3,24" fill="var(--plum)" stroke="#fff" stroke-width="3"/><rect x="27" y="40" width="6" height="18" fill="#fff"/><rect x="36" y="30" width="6" height="28" fill="#fff"/><rect x="45" y="36" width="6" height="22" fill="#fff"/><rect x="54" y="44" width="4" height="14" fill="#fff"/></svg>
    <h3>Loans</h3>
    <p>Duis venenatis nibh ac convallis laoreet. In dignissim imperdiet feugiat. Integer blandit tortor tellus, sed sodales ligula tristique et.</p>
    <a href="#">Read more »</a>
  </div>
</section>

<section class="welcome">
  <div class="skyline abs" role="img" aria-label="Faint city skyline"></div>
  <h1>Welcome to Pellmoor Realty</h1>
  <p style="top:102px">Quisque eu erat urna. In hac habitasse platea dictumst. Ut at lorem at elit congue facilisis. Aliquam malesuada quis dolor sed euismod. Proin sit amet mauris quis magna volutpat semper id vitae augue. Cras consectetur, neque rhoncus cursus commodo, eros sem facilisis orci, vitae cursus eros tellus quis eros. Etiam non accumsan dolor. Pellentesque condimentum sollicitudin augue, in malesuada nulla facilisis eu. Sed elementum commodo urna quis varius. Integer pulvinar sagittis est, eget convallis nunc viverra et. Cras sit amet dignissim magna, id volutpat erat.</p>
  <p style="top:198px">Nulla congue suscipit semper. Quisque a dictum diam. Nulla tristique turpis pretium luctus gravida. Praesent malesuada, magna nec elementum eleifend, arcu quam euismod orci, nec lobortis libero urna luctus ligula. Morbi mauris est, auctor varius pretium id, semper et mi. Aenean egestas mattis rhoncus.</p>
  <div class="abs" style="top:275px;left:534px"><span class="btn">read more</span></div>
</section>

<section class="advisory">
  <h2 class="abs" style="left:172px;top:70px">Advisory &amp; Consulting</h2>
  <svg class="adv-photo abs" viewBox="0 0 194 210" role="img" aria-label="Business team in a meeting">
    <defs><linearGradient id="advFill" x1="0" y1="0" x2="1" y2="1"><stop offset="0" stop-color="#c9ccd2"/><stop offset="1" stop-color="#6c7280"/></linearGradient></defs>
    <polygon points="97,3 190,55 190,155 97,207 4,155 4,55" fill="url(#advFill)" stroke="var(--plum)" stroke-width="4"/>
  </svg>
  <div class="adv-text abs">
    <h3>Non blandit ipsum</h3>
    <p>Phasellus nec dui ut sapien lacinia ornare nec vel nulla.</p>
    <p class="hl">Duis vitae est vel magna imperdiet aliquet. Morbi justo augue.</p>
    <p>convallis vel scelerisque nec, dapibus porta ligula. Nulla congue suscipit semper. Quisque a dictum diam vitae cursus eros tellus quis eros. Etiam non accumsan dolor. Pellentesque condimentum sollicitudin augue, in malesuada nulla facilisis eu.</p>
  </div>
  <div class="abs" style="left:379px;top:434px"><span class="btn" style="width:96px">read more</span></div>

  <div class="team">
    <h2 class="abs" style="left:619px;top:76px">Smart, Honest and Reliable Agents</h2>
    <p class="abs" style="left:619px;top:126px;width:410px;font-size:11px;line-height:15px;color:var(--muted)">Duis vitae est vel magna imperdiet aliquet. Morbi justo augue, convallis vel scelerisque nec, dapibus porta ligula. Nulla congue suscipit semper.</p>
    <div class="agent abs" style="top:186px"><div class="avatar" role="img" aria-label="Agent portrait" style="background:linear-gradient(#d8d8d8,#5a6270)"></div><div><h4>Suspendisse potan</h4><p>Quisque eu erat urna. In hac habitasse platea dictumst.<br>Ut at lorem at</p><a href="#">View Profile</a></div></div>
    <div class="agent abs" style="top:290px"><div class="avatar" role="img" aria-label="Agent portrait" style="background:linear-gradient(#e0e0e0,#4a4a52)"></div><div><h4>Magna imperdiet</h4><p>Quisque eu erat urna. In hac habitasse platea dictumst.<br>Ut at lorem at</p><a href="#">View Profile</a></div></div>
    <div class="agent abs" style="top:394px"><div class="avatar" role="img" aria-label="Agent portrait" style="background:linear-gradient(#e8e4dc,#8a7a6a)"></div><div><h4>Facilisis orci</h4><p>Quisque eu erat urna. In hac habitasse platea dictumst.<br>Ut at lorem at</p><a href="#">View Profile</a></div></div>
  </div>
</section>

<section class="why">
  <div class="why-photo" role="img" aria-label="Modern house exterior under plum overlay"></div>
  <h2>No Hidden Fees and No Gimmicks To Start Saving</h2>
  <div class="sub">Why Use Pellmoor Realty?</div>
  <svg class="abs" style="left:0;top:150px" width="1200" height="110" viewBox="0 0 1200 110">
    <g fill="none" stroke="var(--cream)" stroke-width="5" stroke-linecap="round">
      <path d="M600 4v56"/>
      <path d="M298 110V74q0-14 14-14h576q14 0 14 14v36"/>
      <path d="M600 60v50"/>
    </g>
  </svg>
  <div class="why-col abs" style="left:177px"><h3><span>1.</span>Local Agents</h3><p>Duis vitae est vel magna imperdiet aliquet. Morbi justo augue, convallis vel scelerisque nec, dapibus porta ligula. Nulla congue suscipit semper.</p></div>
  <div class="why-col abs" style="left:475px"><h3><span>2.</span>No Pressure</h3><p>Duis vitae est vel magna imperdiet aliquet. Morbi justo augue, convallis vel scelerisque nec, dapibus porta ligula. Nulla congue suscipit semper.</p></div>
  <div class="why-col abs" style="left:765px"><h3><span>3.</span>Transparent</h3><p>Duis vitae est vel magna imperdiet aliquet. Morbi justo augue, convallis vel scelerisque nec, dapibus porta ligula. Nulla congue suscipit semper.</p></div>
</section>

<section class="testimonials">
  <h2>Over 400 Satisfied Clients Agree,</h2>
  <h3>There is No Better way to Buy a Home</h3>
  <div class="quote abs" style="left:172px;width:276px">Phasellus nec dui ut sapien lacinia ornare nec vel nulla. Duis vitae est vel magna imper diet aliquet. Morbi justo augue, convallis vel scelerisque nec, dapibus porta ligula. Nulla congue suscipit semper. Quisque a dictum diam. Nulla tristique</div>
  <div class="quote abs" style="left:460px;width:280px">Phasellus nec dui ut sapien lacinia ornare nec vel nulla. Duis vitae est vel magna imper diet aliquet. Morbi justo augue, convallis vel scelerisque nec, dapibus porta ligula. Nulla congue suscipit semper. Quisque a dictum diam. Nulla tristique</div>
  <div class="quote abs" style="left:753px;width:275px">Phasellus nec dui ut sapien lacinia ornare nec vel nulla. Duis vitae est vel magna imper diet aliquet. Morbi justo augue, convallis vel scelerisque nec, dapibus porta ligula. Nulla congue suscipit semper. Quisque a dictum diam. Nulla tristique</div>
  <div class="client abs" style="left:190px"><div class="avatar" role="img" aria-label="Client portrait" style="background:linear-gradient(#eee,#6a5a58)"></div>Volutpat semper</div>
  <div class="client abs" style="left:480px"><div class="avatar" role="img" aria-label="Client portrait" style="background:linear-gradient(#eee,#55585e)"></div>Dignissim imperdiet</div>
  <div class="client abs" style="left:775px"><div class="avatar" role="img" aria-label="Client portrait" style="background:linear-gradient(#eee,#4a4e58)"></div>Integer blandit</div>
</section>

<footer class="site-footer">
  <div class="f-col news abs" style="left:177px">
    <h4><i></i>Latest News</h4>
    <div class="date">6th March, 2014</div>
    <p>Nulla congue suscipit semper. Quisque a dictum diam. Nulla tristique turpis pretium luctus gravida. Praesent malesuada</p>
    <div class="date">6th March, 2014</div>
    <p>Nulla congue suscipit semper. Quisque a dictum diam. Nulla tristique turpis pretium luctus gravida.</p>
    <div style="text-align:right;font-size:11px">more »</div>
  </div>
  <div class="f-col contact abs" style="left:493px">
    <h4><i></i>Contact Us</h4>
    <ul>
      <li><i></i>418 Linden Court<br>Millbrook, NJ 07099</li>
      <li><i></i>(866) 555-0142</li>
      <li><i></i>info@pellmoorrealty.com</li>
    </ul>
    <div class="socials"><span></span><span></span><span></span><span></span></div>
  </div>
  <div class="f-col abs" style="left:770px">
    <h4><i></i>Subscribe Newsletter</h4>
    <p style="font-size:11px;line-height:14px">Enter your email address to receive all news from our awesome website</p>
    <div class="sub-field">email address</div>
    <div class="sub-row"><span class="sub-brand">Pellmoor Realty</span><span class="sub-btn">Submit</span></div>
  </div>
</footer>
<div class="copyright" style="position:absolute;left:0;width:1200px">Copyright © 2014, All rights reserved.</div>

</body>
</html>
```